Checkout sign

Wall sign for clinic checkout.
“The Good Lord does ALL the healing..
But we DO collect the co-pay”

Add Celtic cross at top and our logo on bottom

```html
<!DOCTYPE html>
<html lang="en">
<head>
<meta charset="utf-8">
<title>Checkout Sign – Halloran Orthopedic Clinic</title>
<link rel="stylesheet" href="https://fonts.googleapis.com/css2?family=Playfair+Display:ital,wght@0,400;0,700;0,900;1,700&display=swap">
<style>
  :root {
    --royal-blue: #1b0a9e;
    --ink: #121212;
    --paper: #ffffff;
    --paper-shade: #f1f1f4;
    --cross-light: #4a3cc0;
  }
  * { margin: 0; padding: 0; box-sizing: border-box; }
  html, body {
    width: 1110px;
    height: 1200px;
    overflow: hidden;
    background: var(--paper);
  }
  .sign {
    width: 1110px;
    height: 1200px;
    background: var(--royal-blue);
    padding: 42px;
  }
  .sign-panel {
    width: 100%;
    height: 100%;
    background: linear-gradient(160deg, var(--paper) 0%, var(--paper-shade) 45%, var(--paper) 70%, var(--paper-shade) 100%);
    padding: 20px;
  }
  .sign-rule {
    width: 100%;
    height: 100%;
    border: 2px solid var(--royal-blue);
    display: flex;
    flex-direction: column;
    align-items: center;
    padding-top: 48px;
  }
  .cross-art {
    width: 250px;
    height: 380px;
    border-radius: 18px;
    background: linear-gradient(180deg, var(--cross-light), var(--royal-blue));
  }
  .message {
    text-align: center;
    color: var(--ink);
    font-family: 'Playfair Display', serif;
    margin-top: 22px;
  }
  .message-lead {
    display: block;
    font-weight: 700;
    font-size: 62px;
    line-height: 0.9;
    margin-left: -270px;
  }
  .message-title {
    display: block;
    font-weight: 900;
    font-size: 150px;
    line-height: 0.85;
    letter-spacing: -1px;
  }
  .message-line {
    display: block;
    font-style: italic;
    font-weight: 700;
    font-size: 66px;
    line-height: 1.3;
  }
  .clinic-mark {
    margin-top: 26px;
    display: flex;
    flex-direction: column;
    align-items: center;
    color: var(--royal-blue);
    font-family: 'Playfair Display', serif;
  }
  .clinic-mark svg { display: block; }
  .clinic-name {
    margin-top: 8px;
    font-size: 30px;
    font-weight: 400;
    letter-spacing: 1px;
    text-transform: uppercase;
    line-height: 1.1;
    text-align: center;
  }
</style>
</head>
<body>
  <main class="sign">
    <div class="sign-panel">
      <div class="sign-rule">
        <div class="cross-art" role="img" aria-label="Ornate blue Celtic cross with lace-like filigree pattern"></div>

        <h1 class="message">
          <span class="message-lead">The</span>
          <span class="message-title">Good Lord</span>
          <span class="message-line">does ALL the healing...</span>
          <span class="message-line">But we DO</span>
          <span class="message-line">collect the co-pay</span>
        </h1>

        <div class="clinic-mark">
          <svg width="70" height="70" viewBox="0 0 70 70" aria-hidden="true">
            <circle cx="35" cy="35" r="31" fill="none" stroke="var(--royal-blue)" stroke-width="4"/>
          </svg>
          <p class="clinic-name">Halloran Orthopedic Clinic</p>
        </div>
      </div>
    </div>
  </main>
</body>
</html>
```